Business Card Design

Just looking for a good designs that looks good with our company logo. I'd like it to be simple and to the point. Just including contact information, our logo, and my name somewhere on the card so future clients know who they're contacting, and a couple services offered. The two images I attached are pictures of our logo. I don't care which color they they are, I just attached both images to give a reference of logo colors depending on the color of the card.
Names: Calvin Prewitt
Phone: 555-247-9061
Email: tidyturfcrew@mailvista.net
Services offered:
Mowing
Fertilization
Aeration
Bed & tree maintenance
and more.
Industry/Entity Type
Business
Contact Information for Business Card
Names: Calvin Prewitt
Phone: 555-247-9061
Look and feel

```html
<!DOCTYPE html>
<html lang="en">
<head>
<meta charset="utf-8">
<title>Tidy Turf Crew – Business Card</title>
<link rel="stylesheet" href="https://fonts.googleapis.com/css2?family=Noto+Serif:ital,wght@0,400;0,700;1,400&family=Oswald:wght@700&display=swap">
<style>
  :root {
    --paper: #e9eae9;
    --coral: #ee6e52;
    --coral-fade: #fbe3d9;
    --ink: #2f3346;
    --navy: #0f3a6b;
    --green: #1f9a4a;
    --red: #e8503e;
    --maroon: #4a1230;
    --hill-light: #7fb843;
    --hill-dark: #2f7f3c;
    --white: #ffffff;
  }
  * { margin: 0; padding: 0; box-sizing: border-box; }
  html, body { width: 1200px; height: 702px; overflow: hidden; background: var(--paper); }
  .card {
    position: relative;
    width: 1200px;
    height: 702px;
    background: var(--paper);
    font-family: "Noto Serif", Georgia, serif;
    overflow: hidden;
  }
  .contact-band {
    position: absolute;
    display: flex;
    align-items: center;
    justify-content: flex-end;
    gap: 10px;
    padding-right: 50px;
    background: linear-gradient(90deg, var(--coral) 0%, var(--coral-fade) 100%);
    border-radius: 3px;
    color: var(--ink);
  }
  .contact-band::after {
    content: "";
    position: absolute;
    right: 50px;
    width: 16px;
    height: 18px;
    background: var(--navy);
    transform: translateX(22px);
  }
  .contact-band--name { left: 683px; top: 57px; width: 506px; height: 82px; }
  .contact-band--phone { left: 814px; top: 157px; width: 373px; height: 65px; justify-content: flex-start; padding-left: 12px; }
  .contact-band--email { left: 814px; top: 239px; width: 373px; height: 64px; justify-content: flex-start; padding-left: 10px; }
  .person-name { font-size: 35px; letter-spacing: 1px; }
  .phone-number { font-size: 33px; color: #111; letter-spacing: 1px; }
  .email-address { font-size: 21px; font-weight: 700; color: #111; letter-spacing: -0.3px; }
  .phone-icon { width: 32px; height: 32px; flex: none; }

  .guarantee {
    position: absolute;
    left: 147px;
    top: 210px;
    width: 300px;
    height: 80px;
  }
  .guarantee__ribbon {
    position: absolute;
    left: 90px;
    top: 4px;
    width: 206px;
    height: 52px;
    background: linear-gradient(90deg, #ef5a2a 0%, var(--maroon) 100%);
    transform: skewY(-4deg);
    display: flex;
    align-items: center;
    justify-content: center;
    padding-left: 18px;
  }
  .guarantee__ribbon span {
    font-family: "Oswald", "Arial Narrow", sans-serif;
    font-size: 24px;
    color: var(--white);
  }
  .guarantee__percent {
    position: absolute;
    left: 0;
    top: 12px;
    font-family: "Oswald", "Arial Narrow", sans-serif;
    font-size: 46px;
    line-height: 1;
    color: var(--green);
    letter-spacing: -2px;
  }
  .guarantee__quality {
    position: absolute;
    left: 6px;
    top: 68px;
    width: 94px;
    height: 24px;
    background: var(--white);
    color: var(--green);
    font-size: 15px;
    text-align: center;
    line-height: 24px;
    letter-spacing: 1px;
  }

  .brand {
    position: absolute;
    left: 410px;
    top: 270px;
    width: 350px;
    height: 70px;
    display: flex;
    align-items: center;
    justify-content: center;
    gap: 14px;
  }
  .brand__dot { width: 26px; height: 26px; border-radius: 50%; background: var(--red); flex: none; }
  .brand__name { font-size: 42px; font-weight: 700; color: var(--ink); white-space: nowrap; }

  .services {
    position: absolute;
    left: 0;
    top: 455px;
    width: 1190px;
    text-align: center;
    font-style: italic;
    font-size: 35px;
    line-height: 47px;
  }
  .services .green { color: var(--green); }
  .services .red { color: var(--red); }
  .services__line--last { padding-left: 35px; }

  .landscape {
    position: absolute;
    left: 0;
    top: 560px;
    width: 1200px;
    height: 142px;
    background: linear-gradient(180deg, var(--hill-light) 0%, var(--hill-dark) 100%);
    border-radius: 50% 50% 0 0 / 45% 45% 0 0;
  }
</style>
</head>
<body>
  <div class="card">
    <div class="contact-band contact-band--name"><span class="person-name">Calvin Prewitt</span></div>
    <div class="contact-band contact-band--phone">
      <svg class="phone-icon" viewBox="0 0 32 32" aria-hidden="true">
        <rect width="32" height="32" rx="6" fill="var(--navy)"/>
        <path d="M11 7c1 0 2 3 2.5 4.5.3 1-1.5 2-1.5 2.5 0 1.5 3.5 5.5 5 6 .6.2 1.6-1.6 2.6-1.3 1.4.5 4.4 1.8 4.4 2.8 0 1.5-2 3.5-4 3.5C14 25 7 17.5 7 11.5 7 9 9.5 7 11 7z" fill="var(--coral)"/>
      </svg>
      <span class="phone-number">555-247-9061</span>
    </div>
    <div class="contact-band contact-band--email"><span class="email-address">tidyturfcrew@mailvista.net</span></div>

    <div class="guarantee">
      <div class="guarantee__ribbon"><span>Guaranteed</span></div>
      <div class="guarantee__percent">100%</div>
      <div class="guarantee__quality">QUALITY</div>
    </div>

    <div class="brand">
      <span class="brand__dot"></span>
      <span class="brand__name">Tidy Turf Crew</span>
    </div>

    <div class="services">
      <div class="services__line"><span class="green">Mowing</span> <span style="color:#5a6fd0">.</span><span class="red">Fertilization</span> <span class="green">.Aeration</span></div>
      <div class="services__line red">Bed and tree maintenance</div>
      <div class="services__line services__line--last green">and more ...</div>
    </div>

    <div class="landscape" role="img" aria-label="Illustration of rolling green hills with a winding path and small trees"></div>
  </div>
</body>
</html>
```